Lawyer Needs New Atypical Stationery Design With Gravitas

I need new stationery (letterhead, envelopes, note pads, maybe business cards) for my law office. Although I work by myself, for myself, I need stationery that conveys strength, stability, and gravitas. I would also like a design that makes the end user think: "This is unique. I've never seen letterhead like this before." Most importantly, it should not look like many lawyers' letterhead, meaning no scales of justice. My current letterhead (attached) has my name and "Attorney at Law" on it; however, I would like to transition to "HASKE | LAW" or something like that with the new letterhead. Lastly, I would like an envelope design that is not the standard #10 envelope with a triangular back flap, maybe a square flap or something in the style or design that also makes people stop and think "That's different from anything I've seen before."

```html
<!DOCTYPE html>
<html lang="en">
<head>
<meta charset="utf-8">
<title>Haske | Law Stationery</title>
<link rel="stylesheet" href="https://fonts.googleapis.com/css2?family=Montserrat:wght@400;500;700&family=Lato:wght@400;700&display=swap">
<style>
:root{
  --maroon:#690a36;
  --maroon-deep:#5e0830;
  --flap-line:#4d0627;
  --paper:#ffffff;
  --page:#f7f7f7;
  --ink:#1e1e1e;
  --body:#6b6b6b;
  --rule:#9a9a9a;
  --backdrop:#c9c9c9;
}
*{margin:0;padding:0;box-sizing:border-box}
html,body{width:1200px;height:768px;overflow:hidden}
body{background:var(--backdrop);position:relative;font-family:"Montserrat",sans-serif;color:var(--ink)}
.item{position:absolute}
.mark{position:absolute;background:var(--maroon)}
.mark.light{background:var(--paper)}
.wordmark{position:absolute;font-family:"Montserrat",sans-serif;font-weight:500;color:var(--maroon);white-space:nowrap;letter-spacing:.04em}
.wordmark.light{color:var(--paper)}
.icon{width:6px;height:6px;display:inline-block;vertical-align:-1px;margin-right:3px}

/* Letterhead */
.letterhead{left:66px;top:74px;width:425px;height:607px;background:var(--paper)}
.letterhead .mark{left:61px;top:30px;width:36px;height:36px}
.letterhead .wordmark{left:32px;top:73px;font-size:12.5px}
.lh-address{position:absolute;left:185px;top:33px;font-size:7.3px;line-height:11px}
.lh-divider{position:absolute;left:289px;top:34px;width:1px;height:31px;background:var(--maroon)}
.lh-contact{position:absolute;left:295px;top:33px;font-size:7.3px;line-height:11px}
.lh-recipient{position:absolute;left:33px;top:159px}
.lh-recipient h2{font-family:"Lato",sans-serif;font-size:9px;font-weight:700;color:var(--maroon)}
.lh-recipient p{font-family:"Lato",sans-serif;font-size:6.3px;font-weight:700;margin-top:2px}
.lh-date{position:absolute;right:35px;top:171px;font-family:"Lato",sans-serif;font-size:6.3px;color:var(--body)}
.lh-body{position:absolute;left:33px;top:276px;width:360px;font-family:"Lato",sans-serif;font-weight:400;font-size:6.6px;line-height:10.55px;color:var(--body);text-align:justify;hyphens:auto}
.lh-body p{margin-bottom:10.5px}
.lh-signature{position:absolute;left:33px;top:446px;width:92px;height:22px;background:linear-gradient(90deg,#e9e9e9,#f4f4f4);border-radius:3px}

/* Business cards */
.card{width:249px;height:146px;border-radius:8px}
.card-front{left:523px;top:74px;background:var(--paper)}
.card-front .mark{left:188px;top:14px;width:29px;height:29px}
.card-front .wordmark{right:10px;top:48px;font-size:9.5px}
.card-name{position:absolute;left:10px;top:70px;font-size:10px;font-weight:700;color:var(--maroon)}
.card-title{position:absolute;left:11px;top:83px;font-size:5.8px}
.card-rule{position:absolute;left:10px;right:10px;top:96px;height:1px;background:var(--maroon)}
.card-contact{position:absolute;left:10px;top:103px;font-size:5.8px;line-height:9.6px}
.card-address{position:absolute;right:10px;top:103px;font-size:5.8px;line-height:9.6px;text-align:right}
.card-back{left:523px;top:235px;width:250px;height:147px;background:var(--maroon-deep)}
.card-back .mark{left:100px;top:33px;width:52px;height:52px}
.card-back .wordmark{left:0;right:0;text-align:center;top:92px;font-size:18px}

/* Envelopes */
.envelope{width:329px;height:146px;background:var(--maroon-deep)}
.envelope-front{left:798px;top:74px}
.envelope-front .mark{left:35px;top:12px;width:24px;height:24px}
.envelope-front .wordmark{left:15px;top:41px;font-size:8.5px}
.env-address{position:absolute;left:16px;top:54px;font-size:4px;line-height:6.3px;color:var(--paper)}
.envelope-back{left:798px;top:234px;height:147px;background:var(--maroon)}
.envelope-back svg{position:absolute;inset:0}

/* Notebook */
.notebook{left:550px;top:417px;width:188px;height:262px;background:var(--maroon)}
.notebook .mark{left:74px;top:102px;width:40px;height:40px}
.notebook .wordmark{left:0;right:0;text-align:center;top:148px;font-size:14.5px}
.notepad{left:757px;top:415px;width:371px;height:261px;background:var(--page);display:flex}
.note-page{position:relative;flex:1;height:100%}
.note-page + .note-page{border-left:1px solid #b0b0b0}
.note-page .mark{left:30px;top:12px;width:15px;height:15px}
.note-page .wordmark{left:18px;top:30px;font-size:5.5px}
.note-date{position:absolute;right:17px;top:35px;font-size:3.5px;color:var(--body)}
.note-lines{position:absolute;left:18px;right:17px;top:48px;height:188px;background:repeating-linear-gradient(to bottom,transparent 0 9.4px,var(--rule) 9.4px 10.4px)}
</style>
</head>
<body>

<section class="item letterhead">
  <div class="mark"></div>
  <div class="wordmark">HASKE | LAW</div>
  <div class="lh-address">4120 Larkspur Avenue<br>Suite Six Hundred<br>Westbrook, CA 90417-1180</div>
  <div class="lh-divider"></div>
  <div class="lh-contact">
    <div><svg class="icon" viewBox="0 0 10 10"><path fill="#690a36" d="M1 3c0-2 8-2 8 0v1H7V3H3v1H1zM2 5h6l1 4H1z"/></svg>(310) 555-0148</div>
    <div><svg class="icon" viewBox="0 0 10 10"><path fill="#690a36" d="M0 2h10v6H0z"/><path d="M0 2l5 3 5-3" stroke="#fff" fill="none"/></svg>daniel@danielhaske.com</div>
    <div><svg class="icon" viewBox="0 0 10 10"><circle cx="5" cy="5" r="4.5" fill="#690a36"/><path d="M1 5h8M5 1c-2 2-2 6 0 8M5 1c2 2 2 6 0 8" stroke="#fff" stroke-width=".7" fill="none"/></svg>www.danielhaske.com</div>
  </div>
  <div class="lh-recipient">
    <h2>Dear. Mrs Clara Ann Moreno</h2>
    <p>Chief Director</p>
  </div>
  <div class="lh-date">Date: 02-July-2025</div>
  <div class="lh-body" style="top:203px">
    <p>Lorem ipsum dolor sit amet, consectetur adipiscing elit, sed do eiusmod tempor incididunt ut labore et dolore magna aliqua. Sollicitudin ac orci phasellus egestas tellus rutrum tellus. Euismod elementum nisi quis eleifend quam adipiscing vitae proin sagittis. Egestas sed tempus urna et pharetra pharetra. Quis blandit turpis cursus in hac habitasse. Sed velit dignissim sodales ut eu. Ac auctor augue mauris augue neque. In arcu cursus euismod quis viverra nibh cras pulvinar mattis. Libero justo laoreet sit amet. Felis eget nunc lobortis mattis aliquam faucibus purus in. Pulvinar etiam non quam lacus suspendisse faucibus. Odio tempor orci dapibus ultrices. Velit dignissim sodales ut eu sem integer vitae justo. Fermentum et sollicitudin ac orci phasellus egestas. Pharetra vel turpis nunc eget lorem dolor sed. Sed turpis tincidunt id aliquet risus feugiat in ante. Mus mauris vitae ultricies leo integer malesuada nunc vel. Rhoncus urna neque viverra justo nec ultrices dui. Ut placerat orci nulla pellentesque dignissim enim sit amet.</p>
    <p>Bibendum arcu vitae elementum curabitur vitae nunc. Nunc pulvinar sapien et ligula ullamcorper malesuada. At elementum eu facilisis sed. Erat pellentesque adipiscing commodo elit at imperdiet dui accumsan sit. Nunc scelerisque viverra mauris in aliquam sem fringilla. In vitae turpis massa sed. Volutpat ac tincidunt vitae semper quis lectus nulla at. Massa placerat duis ultricies lacus sed turpis. Dui vivamus arcu felis bibendum ut tristique et egestas. Blandit aliquam etiam erat velit scelerisque in dictum non consectetur. Id neque aliquam vestibulum morbi blandit cursus risus at. Sed egestas egestas fringilla phasellus faucibus scelerisque eleifend donec. Ornare quam viverra orci sagittis eu volutpat odio facilisis. Volutpat sed cras ornare arcu dui vivamus arcu. Interdum consectetur libero id faucibus nisl.</p>
    <p>Viverra mauris in aliquam sem. Mattis molestie a iaculis at erat pellentesque adipiscing commodo elit. Sit amet volutpat consequat mauris nunc. Aliquam nulla facilisi cras fermentum. Sed turpis tincidunt id aliquet risus feugiat. Augue neque gravida in fermentum et sollicitudin ac orci.</p>
  </div>
  <div class="lh-signature" role="img" aria-label="Handwritten signature of the sender"></div>
</section>

<section class="item card card-front">
  <div class="mark"></div>
  <div class="wordmark">HASKE | LAW</div>
  <div class="card-name">DANIEL HASKE</div>
  <div class="card-title">Attorney At Law</div>
  <div class="card-rule"></div>
  <div class="card-contact">
    <div><svg class="icon" viewBox="0 0 10 10"><path fill="#690a36" d="M1 3c0-2 8-2 8 0v1H7V3H3v1H1zM2 5h6l1 4H1z"/></svg>(310) 555-0148</div>
    <div><svg class="icon" viewBox="0 0 10 10"><path fill="#690a36" d="M0 2h10v6H0z"/><path d="M0 2l5 3 5-3" stroke="#fff" fill="none"/></svg>daniel@danielhaske.com</div>
    <div><svg class="icon" viewBox="0 0 10 10"><circle cx="5" cy="5" r="4.5" fill="#690a36"/><path d="M1 5h8M5 1c-2 2-2 6 0 8M5 1c2 2 2 6 0 8" stroke="#fff" stroke-width=".7" fill="none"/></svg>www.danielhaske.com</div>
  </div>
  <div class="card-address">4120 Larkspur Avenue<br>Suite Six Hundred<br>Westbrook, CA 90417-1180</div>
</section>

<section class="item card card-back">
  <div class="mark light"></div>
  <div class="wordmark light">HASKE | LAW</div>
</section>

<section class="item envelope envelope-front">
  <div class="mark light"></div>
  <div class="wordmark light">HASKE | LAW</div>
  <div class="env-address">4120 Larkspur Avenue<br>Suite Six Hundred<br>Westbrook, CA 90417-1180</div>
</section>

<section class="item envelope envelope-back">
  <svg viewBox="0 0 329 147" width="329" height="147">
    <path d="M0 0 V84 Q0 92 8 92 H321 Q329 92 329 84 V0" fill="#640933" stroke="var(--flap-line)" stroke-width="1"/>
    <path d="M0 147 L40 118 M329 147 L289 118" fill="none" stroke="var(--flap-line)" stroke-width="1"/>
  </svg>
</section>

<section class="item notebook">
  <div class="mark light"></div>
  <div class="wordmark light">HASKE | LAW</div>
</section>

<section class="item notepad">
  <div class="note-page">
    <div class="mark"></div>
    <div class="wordmark">HASKE | LAW</div>
    <div class="note-date">Date:......./......./.........</div>
    <div class="note-lines"></div>
  </div>
  <div class="note-page">
    <div class="mark"></div>
    <div class="wordmark">HASKE | LAW</div>
    <div class="note-date">Date:......./......./.........</div>
    <div class="note-lines"></div>
  </div>
</section>

</body>
</html>
```